Holvik Cabinets Quality Custom Built Kitchens, Vanity Units, Robes ect

Hi,
Was after a new design for our business cards,
we are a cabinet making business and pride ourselves in quality custom built Kitchens, Vanity units, robes ect.
we have been around for over 20 years and we are trying to modernize our card logo.
Looking for something eye catching, bold and exciting
family ran and operated business, we work with builders and also have a large private clientel.

Thanks

Industry/Entity Type

Business

Contact Information for Business Card

Holvik Cabinets

Font styles to use
Serif
Script

Requirements
Must have
• Corinne 0461735928 hvcabinets@mailvane.com
• Po Box 2786
• 5B Wattlebark Court Marrowick Vic 3917
• Phone (03)59286417 Fax (03) 59286942
Nice to have
• Quality Custom Built Kitchens & Vanity Units

```html
<!DOCTYPE html>
<html lang="en">
<head>
<meta charset="utf-8">
<title>Holvik Cabinets – Business Cards</title>
<link rel="stylesheet" href="https://fonts.googleapis.com/css2?family=Josefin+Sans:wght@600&family=Open+Sans:wght@400;700&display=swap">
<style>
  :root {
    --backdrop: #24262b;
    --maroon: #5f3b42;
    --paper: #ffffff;
    --ink: #111111;
    --ink-soft: #2b2b2b;
    --edge: #000000;
  }
  * { margin: 0; padding: 0; box-sizing: border-box; }
  html, body { width: 1200px; height: 900px; overflow: hidden; }
  body {
    background: var(--backdrop);
    font-family: "Open Sans", Arial, sans-serif;
    position: relative;
  }
  .card {
    position: absolute;
    width: 540px;
    height: 309px;
    overflow: hidden;
    box-shadow: 0 14px 30px rgba(0,0,0,0.45);
  }
  .card--front { left: 40px; top: 296px; background: var(--paper); }
  .card--back  { left: 620px; top: 296px; background: var(--maroon); }

  .band { position: absolute; left: 0; width: 100%; }
  .band svg { position: absolute; inset: 0; width: 100%; height: 100%; }

  .card--front .band { top: 128px; height: 104px; }

  .brand {
    position: absolute;
    left: 62px;
    font-family: "Josefin Sans", "Futura", sans-serif;
    font-weight: 600;
    font-size: 38px;
    letter-spacing: 1px;
    color: var(--paper);
    white-space: nowrap;
    line-height: 1;
  }
  .tagline {
    position: absolute;
    left: 66px;
    font-family: "Josefin Sans", "Futura", sans-serif;
    font-weight: 600;
    font-size: 13.5px;
    color: var(--ink);
    white-space: nowrap;
    line-height: 1;
  }
  .card--front .brand { top: 150px; }
  .card--front .tagline { top: 194px; }

  .card--back .brand { top: 44px; }
  .card--back .tagline { top: 88px; }
  .card--back .band { top: 108px; height: 74px; }

  .holder {
    position: absolute;
    left: 66px;
    top: 120px;
    font-weight: 700;
    font-size: 24px;
    color: var(--ink-soft);
    line-height: 1;
  }
  .address {
    position: absolute;
    left: 66px;
    top: 156px;
    font-size: 12.5px;
    color: var(--ink-soft);
    white-space: nowrap;
  }
  .contacts {
    position: absolute;
    left: 66px;
    top: 196px;
    list-style: none;
    color: var(--paper);
    font-size: 15px;
    line-height: 22px;
  }
  .contacts li { display: flex; align-items: center; gap: 10px; }
  .contacts svg { width: 15px; height: 15px; flex: none; }
</style>
</head>
<body>

<section class="card card--front" aria-label="Card front">
  <div class="band">
    <svg viewBox="0 0 540 104" preserveAspectRatio="none" aria-hidden="true">
      <polygon points="0,0 540,0 540,104 0,104" fill="var(--edge)"/>
      <polygon points="10,0 530,0 522,104 18,104" fill="var(--maroon)"/>
    </svg>
  </div>
  <div class="brand">HOLVIK CABINETS</div>
  <div class="tagline">Quality Custom Built Kitchens &amp; Vanity Units</div>
</section>

<section class="card card--back" aria-label="Card back">
  <div class="brand">HOLVIK CABINETS</div>
  <div class="tagline">Quality Custom Built Kitchens &amp; Vanity Units</div>
  <div class="band">
    <svg viewBox="0 0 540 74" preserveAspectRatio="none" aria-hidden="true">
      <polygon points="50,0 540,0 540,74 50,74" fill="var(--edge)"/>
      <polygon points="50,0 530,0 522,74 50,74" fill="var(--paper)"/>
    </svg>
  </div>
  <div class="holder">Corinne</div>
  <div class="address">Po Box 2786 5B Wattlebark Court Marrowick Vic 3917</div>
  <ul class="contacts">
    <li>
      <svg viewBox="0 0 16 16" aria-hidden="true"><rect x="4" y="1" width="8" height="14" rx="1.5" fill="none" stroke="currentColor" stroke-width="1.4"/><circle cx="8" cy="12.5" r="0.9" fill="currentColor"/></svg>
      <span>0461735928</span>
    </li>
    <li>
      <svg viewBox="0 0 16 16" aria-hidden="true"><rect x="4" y="1.5" width="8" height="5" fill="none" stroke="currentColor" stroke-width="1.3"/><rect x="1.5" y="6.5" width="13" height="7" rx="1" fill="currentColor"/><rect x="4" y="11" width="8" height="3.5" fill="var(--maroon)"/></svg>
      <span>(03) 59286942</span>
    </li>
    <li>
      <svg viewBox="0 0 16 16" aria-hidden="true"><path d="M3.5 1.5 L6 1.5 L7 5 L5.3 6.3 C6.2 8.3 7.7 9.8 9.7 10.7 L11 9 L14.5 10 L14.5 12.5 C14.5 13.6 13.6 14.5 12.5 14.5 C6.9 14.5 1.5 9.1 1.5 3.5 C1.5 2.4 2.4 1.5 3.5 1.5 Z" fill="currentColor"/></svg>
      <span>(03)59286417</span>
    </li>
    <li>
      <svg viewBox="0 0 16 16" aria-hidden="true"><rect x="1.5" y="3.5" width="13" height="9" fill="none" stroke="currentColor" stroke-width="1.4"/><path d="M1.5 3.5 L8 9 L14.5 3.5" fill="none" stroke="currentColor" stroke-width="1.4"/></svg>
      <span>hvcabinets@mailvane.com</span>
    </li>
  </ul>
</section>

</body>
</html>
```